New User Registration Welcome/Walkthrough Sequence

We have a group communications app that needs to display a simple and informative series of distinct visuals that can help explain the value of our app and how it works quickly and easily to our new users. A short phrase may be used as a caption for each visual, but the graphic itself should convey most of the concept as described below in the same order explained below.

Users are linked to their electeds leaders and their town/state/country groups. Users can also create or join any other groups. Users can create posts in any of their groups, which can be seen by all group members. When a user creates a post, only his followers get a push notification at first. Posts can be upvoted or downvoted by anyone in the group. If a post gets enough votes, it is "boosted" - that means that all group members will receive push notification alert.

We think this can be described in a series of 5-8 simple images. We plan to display these images as an automated sequence after a new user completes user registration. Probably fade-in/fade-out from one to the next automatically. We prefer a design that takes up 1/2 to 3/4 of the screen (not full screen).

Some ideas that we've had (just suggestions - we are looking for your creativity!):
For elected leaders: small stock avatars of real people could work
For groups: group icons could work
For notifications: concentric, fading rings around the avatar of the user(s) receiving the notification
For followers: smiley avatar
For non-follower group members: anonymous avatar

Ideally, each image should be strong enough to stand on its own in case we want to use an individual image somewhere else in the app. However, we do plan to sequence them one after-another for the user welcome after successful registration.

Target Market(s)

A broad audience of mobile app users.

Industry/Entity Type

Communications

Font styles to use
Sans Serif

Colors

Designer to choose colors to be used in the design.

Requirements
Must have
• The series of images must adequately explain: "Users are linked to their electeds leaders and their town/state/country groups. Users can also create or join any other groups. Users can create posts in any of their groups, which can be seen by all group members. When a user creates a post, only his followers get a push notification at first. Posts can be upvoted or downvoted by anyone in the group. If a post gets enough votes, it is "boosted" - that means that all group members will receive push notification alert."
• The images should be expected to be viewed on no larger than 3/4 of a mobile screen size.
Nice to have
• Some ideas that we've had (just suggestions - we are looking for your creativity!):
• For elected leaders: small stock avatars of real people could work
• For groups: group icons could work
• For notifications: concentric, fading rings around the avatar of the user(s) receiving the notification
• For followers: smiley avatar
• For non-follower group members: anonymous avatar
• However, you can come up with your own ideas too! A modern / flat design is preferred.
• Ideally, each image should be strong enough to stand on its own in case we want to use an individual image somewhere else in the app. However, we do plan to sequence them one after-another for the user welcome after successful registration.
Should not have
• Should not be complex. These screens should be designed to look at very quickly as part of the new user experience.
• The images should *NOT* be full screen. They should *NOT* be app screens. They should *not* be text heavy.

```html
<!DOCTYPE html>
<html lang="en">
<head>
<meta charset="utf-8">
<title>Power in Numbers</title>
<link href="https://fonts.googleapis.com/css2?family=Roboto:wght@400;700;900&display=swap" rel="stylesheet">
<style>
  :root {
    --bg: #8dc63f;
    --status: #7db33a;
    --ring: #7ab139;
    --disc: #658f2e;
    --upvote: #fff000;
    --downvote: #ffcf40;
    --ink-dark: #4b6d12;
    --ink-mid: #5d8520;
    --white: #ffffff;
    --button-edge: #6a9f2e;
    --logo-ink: #111111;
  }
  * { box-sizing: border-box; margin: 0; padding: 0; }
  html, body { width: 675px; height: 1200px; overflow: hidden; }
  body {
    background: var(--bg);
    font-family: "Roboto", Arial, sans-serif;
    position: relative;
  }
  .status-bar {
    position: absolute; top: 0; left: 0; width: 675px; height: 45px;
    background: var(--status);
  }
  .status-icons { position: absolute; top: 0; left: 0; }
  .status-time {
    position: absolute; right: 16px; top: 9px;
    color: var(--white); font-size: 24px; font-weight: 400;
  }
  .headline {
    position: absolute; top: 148px; width: 100%; text-align: center;
    color: var(--white); font-size: 27px; font-weight: 700; letter-spacing: 0.2px;
  }
  .subline {
    position: absolute; top: 190px; width: 100%; text-align: center;
    color: var(--ink-mid); font-size: 20.5px; font-weight: 400;
  }
  .group-label {
    position: absolute; top: 278px; width: 100%; text-align: center;
    color: var(--ink-dark); font-size: 20px; font-weight: 700;
  }
  .vote-gauge { position: absolute; top: 0; left: 0; }
  .gauge-label {
    fill: var(--ink-dark); font-size: 18px; font-weight: 900;
    font-family: "Roboto", Arial, sans-serif;
  }
  .brand-name {
    fill: var(--logo-ink); font-size: 19px; font-weight: 900;
    font-family: "Roboto", Arial, sans-serif;
  }
  .prompt {
    position: absolute; top: 757px; width: 100%; text-align: center;
    color: var(--ink-mid); font-size: 17px;
  }
  .prompt strong { font-weight: 700; }
  .cta-button {
    position: absolute; left: 192px; top: 864px; width: 290px; height: 94px;
    background: var(--white); border: 3px solid var(--button-edge);
    border-radius: 22px;
    display: flex; align-items: center; justify-content: center;
    color: var(--bg); font-size: 25px; font-weight: 700;
  }
</style>
</head>
<body>
  <header class="status-bar">
    <svg class="status-icons" width="675" height="45" viewBox="0 0 675 45" aria-hidden="true">
      <path d="M470 16 L494 16 L482 33 Z" fill="var(--white)"/>
      <path d="M518 34 L540 34 L540 12 Z" fill="var(--white)" opacity="0.55"/>
      <path d="M518 34 L530 34 L530 23 Z" fill="var(--white)"/>
      <rect x="566" y="10" width="14" height="24" rx="2" fill="var(--white)" opacity="0.55"/>
      <rect x="566" y="21" width="14" height="13" rx="1" fill="var(--white)"/>
    </svg>
    <span class="status-time">12:30</span>
  </header>

  <h1 class="headline">POWER IN NUMBERS</h1>
  <p class="subline">Boosted posts unlock powerful insights</p>
  <h2 class="group-label">SENATOR SMITH'S CONSTITUENTS</h2>

  <svg class="vote-gauge" width="675" height="1200" viewBox="0 0 675 1200" role="img" aria-label="Vote gauge: 75% upvote, 25% down vote">
    <defs>
      <path id="upvote-path" d="M170.7 435.5 A203 203 0 0 1 438.5 376.2"/>
      <path id="downvote-path" d="M533.9 502.9 A203 203 0 0 1 492.5 682.5"/>
    </defs>
    <circle cx="337" cy="552" r="171" fill="var(--ring)"/>
    <circle cx="337" cy="552" r="162" fill="var(--disc)"/>
    <path d="M205.2 698.4 A197 197 0 1 1 519 476.6" fill="none" stroke="var(--upvote)" stroke-width="19"/>
    <path d="M523.3 487.9 A197 197 0 0 1 470.1 697.2" fill="none" stroke="var(--downvote)" stroke-width="19"/>
    <text class="gauge-label"><textPath href="#upvote-path" startOffset="8">75% UPVOTE</textPath></text>
    <text class="gauge-label"><textPath href="#downvote-path" startOffset="4">25% DOWN VOTE</textPath></text>

    <g fill="none" stroke="var(--white)" stroke-width="1">
      <circle cx="337" cy="552" r="108" stroke-dasharray="70 18 30 14"/>
      <circle cx="337" cy="552" r="100" stroke-dasharray="4 4" opacity="0.9"/>
      <circle cx="337" cy="552" r="90" stroke-dasharray="120 30"/>
    </g>
    <circle cx="337" cy="552" r="80" fill="var(--white)"/>
    <text class="brand-name" x="337" y="547" text-anchor="middle">CIVIC</text>
    <text class="brand-name" x="337" y="571" text-anchor="middle">CIRCLE</text>
  </svg>

  <p class="prompt">Ready to get involved? Tap the "<strong>Let's Go</strong>" button!</p>
  <div class="cta-button">Let's GO</div>
</body>
</html>
```